Owen Talvik actor business cards

I need unique and interesting business cards that have my headshot photo, my name, tagline/position/skills, contact info, preferred pronouns (he, him, his), and social media handles. These need to be memorable networking tools to hand out at events that stand out. I am an actor that works in theatre, film, and TV and usually play darker dramatic roles, though it doesn't have to necessarily need to be reflected in the design, but I am not a light, comedic actor. In my email tagline, My position/skills are "Actor, storyteller, theatre maker."

Target Market(s)

Casting directors, film and television community, theatre community.

Industry/Entity Type

Performing Art

Contact Information for Business Card

Owen Talvik. Pronouns: he, him, his. Contact info: (555)-310-7826, Owentalvik.example, owentalvik@mailbox.example. Talent representation: Brindlecove Talent Agency. Social Media: Facebook page, twitter and instagram: @OwenTalvikPlays. Company Member of Harrowgate Theatre Company.

Font styles to use
Serif
Decorative

Colors

Designer to choose colors to be used in the design.

Requirements
Must have
• Headshot photo, name, tagline, preferred pronouns, contact info, Social media handle, talent agency logo, harrowgate theatre company logo. Both logos should be smaller than my name. Under or near Harrowgate logo, it should say "Company Member"
Nice to have
• I would like to have the photo, my name, tagline, and maybe pronouns on one side, and all contact info, and social media, and talent agency logo on the other. I would like the style to reflect my type which is a little more serious and somewhat darker, and definitely not comedic.
Should not have
• No extraneous theatre lights, camera, or film, etc. clip art or photos. Use solid backgrounds or photos provided.

```html
<!DOCTYPE html>
<html lang="en">
<head>
<meta charset="utf-8">
<title>Owen Talvik – Business Card</title>
<link rel="stylesheet" href="https://fonts.googleapis.com/css2?family=Arimo:wght@400&family=Caudex:ital,wght@0,400;1,400&display=swap">
<style>
  :root {
    --page-bg: #e6e4e1;
    --panel-bg: #f3f4f4;
    --ink: #1c1c1c;
    --name-blue: #2b9bd9;
    --pronoun-teal: #237f9c;
    --icon-blue: #2a9ad8;
    --rule: #a3a6a8;
    --photo-dark: #2b2624;
    --photo-shirt: #4c6499;
    --photo-teal: #3d7f86;
  }
  * { margin: 0; padding: 0; box-sizing: border-box; }
  html, body {
    width: 1200px; height: 900px; overflow: hidden;
    background: var(--page-bg);
  }
  .card {
    position: absolute; left: 78px; top: 128px;
    width: 1043px; height: 645px;
    background: var(--panel-bg);
    box-shadow: 0 10px 30px rgba(0,0,0,0.18);
    overflow: hidden;
  }
  .headshot {
    position: absolute; left: 0; top: 0; width: 514px; height: 100%;
    background:
      linear-gradient(180deg, rgba(0,0,0,0) 55%, var(--photo-shirt) 56%),
      linear-gradient(90deg, var(--photo-dark) 0%, #5a4a42 30%, #8c7466 50%, #6b6f73 72%, var(--photo-teal) 82%, #4a8a90 100%);
  }
  .details {
    position: absolute; left: 514px; top: 0; right: 0; bottom: 0;
    font-family: "Arimo", Arial, sans-serif; color: var(--ink);
  }
  .agency-mark {
    position: absolute; left: 35px; top: 58px;
    font-family: "Caudex", Georgia, serif; font-style: normal; color: var(--ink);
    display: flex; align-items: center; gap: 12px;
  }
  .agency-mark .dot { width: 22px; height: 22px; border-radius: 50%; background: var(--ink); }
  .agency-name { font-size: 44px; line-height: 1; }
  .agency-sub { font-size: 44px; line-height: 1; }
  .agency-tag {
    position: absolute; left: 35px; width: 290px; top: 118px;
    font-family: "Caudex", Georgia, serif; font-size: 17px; text-align: right; color: var(--ink);
  }
  .name {
    position: absolute; left: 35px; top: 226px;
    font-family: "Caudex", Georgia, serif; font-style: italic;
    font-size: 48px; color: var(--name-blue); line-height: 1;
  }
  .tagline { position: absolute; left: 35px; top: 287px; font-size: 25px; }
  .rule { position: absolute; left: 35px; width: 440px; height: 2px; background: var(--rule); }
  .rule-1 { top: 327px; } .rule-2 { top: 461px; } .rule-3 { top: 537px; }
  .contact { position: absolute; left: 35px; top: 345px; list-style: none; }
  .contact li { display: flex; align-items: center; gap: 8px; font-size: 25px; height: 34.5px; }
  .contact svg { width: 20px; height: 20px; flex: none; }
  .social { position: absolute; left: 35px; top: 484px; display: flex; align-items: center; gap: 6px; font-size: 27px; }
  .social .circle { width: 34px; height: 34px; border-radius: 50%; background: var(--icon-blue); }
  .social .handle { margin-left: 8px; }
  .pronouns {
    position: absolute; left: 35px; top: 553px;
    font-family: "Caudex", Georgia, serif; font-style: italic;
    font-size: 46px; color: var(--pronoun-teal); line-height: 1;
  }
</style>
</head>
<body>
  <section class="card">
    <div class="headshot" role="img" aria-label="Headshot photo of Owen Talvik in a blue shirt"></div>
    <div class="details">
      <div class="agency-mark">
        <span class="dot"></span>
        <span class="agency-name">Brindlecove</span>
      </div>
      <div class="agency-tag">Talent Agency</div>
      <h1 class="name">Owen Talvik</h1>
      <p class="tagline">Actor, Storyteller, Theatre Maker</p>
      <div class="rule rule-1"></div>
      <ul class="contact">
        <li>
          <svg viewBox="0 0 20 20" aria-hidden="true"><path fill="var(--icon-blue)" d="M5 3l3 3-2 2c1 2 3 4 5 5l2-2 3 3-2 3C8 17 3 12 2 5z"/></svg>
          555-310-7826
        </li>
        <li>
          <svg viewBox="0 0 20 20" aria-hidden="true"><rect x="2" y="4" width="16" height="12" fill="var(--icon-blue)"/><path d="M2 4l8 7 8-7" fill="none" stroke="#fff" stroke-width="1.5"/></svg>
          owentalvik@mailbox.example
        </li>
        <li>
          <svg viewBox="0 0 20 20" aria-hidden="true"><circle cx="10" cy="10" r="8" fill="var(--icon-blue)"/><path d="M2 10h16M10 2c3 3 3 13 0 16M10 2c-3 3-3 13 0 16" fill="none" stroke="#fff" stroke-width="1.2"/></svg>
          www.Owentalvik.example
        </li>
      </ul>
      <div class="rule rule-2"></div>
      <div class="social">
        <span class="circle"></span><span class="circle"></span><span class="circle"></span>
        <span class="handle">@OwenTalvikPlays</span>
      </div>
      <div class="rule rule-3"></div>
      <p class="pronouns">He, Him, His</p>
    </div>
  </section>
</body>
</html>
```